brikMOSA corporation pty ltd

Contruction industry
It's a wall and floor tiling business

Industry/Entity Type

Business

Requirements
Must have
• Likes-
- clean and easy to read
- a witty design is always well received
- for it to look reputable in the industry
- a strong and direct presentation
- simple but striking colour selection
Should not have
• Dislikes-
- pls no tacky square tiles to resemble tiling

```html
<!DOCTYPE html>
<html lang="en">
<head>
<meta charset="utf-8">
<title>brikMOSA corporation pty ltd – Business Card</title>
<link rel="stylesheet" href="https://fonts.googleapis.com/css2?family=Old+Standard+TT:wght@400&display=swap">
<style>
  :root {
    --card-black: #060606;
    --brand-amber: #ffab00;
    --ink: #0a0a0a;
  }
  html, body {
    margin: 0;
    padding: 0;
    width: 1200px;
    height: 686px;
    overflow: hidden;
    background: var(--card-black);
  }
  .card {
    position: relative;
    width: 1200px;
    height: 686px;
    background: var(--card-black);
    font-family: "Old Standard TT", "Times New Roman", serif;
    overflow: hidden;
  }
  .amber-arc {
    position: absolute;
    inset: 0;
    width: 1200px;
    height: 686px;
  }
  .brand-name {
    position: absolute;
    left: 0;
    top: 236px;
    width: 646px;
    margin: 0;
    text-align: center;
    font-size: 100px;
    font-weight: 400;
    line-height: 1;
    letter-spacing: 4px;
    color: var(--ink);
  }
  .brand-sub {
    position: absolute;
    left: 0;
    top: 348px;
    width: 674px;
    margin: 0;
    text-align: center;
    font-size: 46px;
    line-height: 1;
    color: var(--ink);
  }
  .info {
    position: absolute;
    margin: 0;
    line-height: 1;
    color: var(--brand-amber);
    white-space: nowrap;
  }
  .service { left: 680px; top: 38px; font-size: 50px; }
  .director { left: 691px; top: 290px; font-size: 50px; }
  .phone { left: 800px; top: 527px; font-size: 52px; }
  .email { left: 798px; top: 612px; font-size: 38px; }
  .icon {
    position: absolute;
  }
  .icon-phone { left: 705px; top: 520px; }
  .icon-mail { left: 706px; top: 602px; }
</style>
</head>
<body>
  <main class="card">
    <svg class="amber-arc" viewBox="0 0 1200 686" aria-hidden="true">
      <path d="M0 0 H520 C610 110 668 240 661 366 C655 480 630 590 594 686 H0 Z" fill="var(--brand-amber)"/>
    </svg>

    <h1 class="brand-name">BRIKMOSA</h1>
    <p class="brand-sub">corporation pty ltd</p>

    <p class="info service">Wall and floor tiling</p>
    <p class="info director">Director: Nik Varos</p>

    <svg class="icon icon-phone" width="78" height="52" viewBox="0 0 78 52" aria-hidden="true">
      <path d="M2 16 C4 4 20 0 39 0 C58 0 74 4 76 16 L76 20 L60 20 L58 12 L20 12 L18 20 L2 20 Z" fill="var(--brand-amber)"/>
      <path d="M20 18 H58 L70 40 V52 H8 V40 Z" fill="var(--brand-amber)"/>
      <circle cx="39" cy="35" r="10" fill="var(--card-black)"/>
      <circle cx="39" cy="35" r="4" fill="var(--brand-amber)"/>
    </svg>
    <p class="info phone">0400 555 01</p>

    <svg class="icon icon-mail" width="74" height="56" viewBox="0 0 74 56" aria-hidden="true">
      <rect x="2" y="2" width="70" height="52" fill="none" stroke="var(--brand-amber)" stroke-width="3"/>
      <path d="M2 2 L37 32 L72 2 M2 54 L28 25 M72 54 L46 25" fill="none" stroke="var(--brand-amber)" stroke-width="3"/>
    </svg>
    <p class="info email">nik.varos@mail.com</p>
  </main>
</body>
</html>
```